Kestrel.vc needs a better website design!

We need a new and better website for Kestrel.vc. We're a Canadian venture capital firm that invests in innovative entrepreneurs. We compete against the following websites: lumora.vc, brightvalefund.ca, osprovc.com, and tessara.vc. We're a diverse group of partners and we're dedicated to the founders we invest in.
Updates

I don’t really like stock photos of random people as part of the website design…so please try to stay away from using those images. Thanks, Owen

Target Market(s)

Canadian entrepreneurs and investors

Industry/Entity Type

Venture capital, finance, investment, entrepreneurship

Coding

Coded - Design and coding required

Number of Pages Required

4 page

Font styles to use
Sans Serif

Colors

Designer to choose colors to be used in the design.

Requirements
Must have
• Clean crisp overall design. Fast and to the point.
Nice to have
• Check out www.kestrel.vc - I did it myself and it is too basic and too wordy.
Should not have
• No stock images with random people in them! Not too wordy or with too many large images that are slow to load.

```html
<!DOCTYPE html>
<html lang="en">
<head>
<meta charset="UTF-8">
<title>Kestrel.vc — Venture Capital</title>
<link href="https://fonts.googleapis.com/css2?family=Open+Sans:wght@400;600;700;800&family=Oswald:wght@400&display=swap" rel="stylesheet">
<style>
:root{
  --green:#7a9a2c;
  --green-dark:#5f7d1c;
  --ink:#222;
  --text:#555;
  --white:#fff;
  --paper:#f4f4f4;
}
*{box-sizing:border-box;margin:0;padding:0}
html,body{width:1200px;height:3666px;overflow:hidden}
body{position:relative;font-family:"Open Sans",sans-serif;color:var(--text);background:var(--white)}
.abs{position:absolute}

/* header */
.site-header{position:absolute;left:0;top:0;width:1200px;height:85px;background:var(--white);z-index:5}
.brand-box{position:absolute;left:100px;top:0;width:135px;height:124px;background:var(--white);text-align:center;padding-top:12px}
.brand-dot{width:66px;height:66px;border-radius:50%;border:4px solid var(--green);margin:0 auto}
.brand-name{font-weight:800;font-size:20px;color:var(--green);margin-top:8px;letter-spacing:.3px}
.main-nav{position:absolute;left:278px;top:35px;display:flex;gap:40px;font-size:12px;font-weight:700;color:var(--ink)}
.call{position:absolute;left:893px;top:18px;display:flex;align-items:center;gap:12px}
.call-icon{width:46px;height:46px;border-radius:50%;background:var(--green);display:flex;align-items:center;justify-content:center}
.call-label{font-family:"Oswald",sans-serif;font-size:13px;color:var(--green)}
.call-number{font-size:24px;font-weight:600;color:var(--ink);line-height:1}

/* hero */
.hero-photo{position:absolute;left:0;top:85px;width:1200px;height:690px;background:linear-gradient(100deg,#7c8a94 0%,#a9b2b8 35%,#6e7f95 60%,#3f5370 100%)}
.hero-circle{position:absolute;left:91px;top:155px;width:464px;height:464px;border-radius:50%;background:rgba(40,40,40,.55);text-align:center;color:var(--white);padding-top:90px}
.hero-circle h2{font-size:31px;font-weight:600;line-height:40px}
.hero-circle h1{font-size:72px;font-weight:700;line-height:1;margin-top:2px}
.hero-circle p{font-size:13px;line-height:28px;margin-top:10px;white-space:nowrap}
.btn{display:inline-block;background:var(--green);color:var(--white);font-weight:700;font-size:15px;border-radius:30px;text-align:center}
.hero-circle .btn{width:214px;height:54px;line-height:54px;margin-top:18px}
.dots{position:absolute;left:574px;top:698px;display:flex;gap:3px}
.dots span{width:10px;height:10px;border-radius:50%;background:var(--white)}
.dots span:first-child{background:var(--green)}

/* about */
.section-title{font-weight:700;color:var(--ink);text-align:center;font-size:32px}
.section-title em{font-style:normal;color:var(--green)}
.about{position:absolute;left:0;top:822px;width:1200px;text-align:center}
.about-lead{font-size:13px;font-weight:700;color:var(--ink);line-height:28px;margin-top:10px}
.about-body{font-size:13px;line-height:28px;margin-top:12px;white-space:nowrap}
.about .btn{width:223px;height:54px;line-height:54px;margin-top:20px}

/* team */
.team-photo{position:absolute;left:0;top:1240px;width:1200px;height:690px;background:linear-gradient(120deg,#1e2c22,#33443a 50%,#1a2620)}
.team-title{position:absolute;left:0;top:1362px;width:1200px;text-align:center;font-size:32px;font-weight:700;color:var(--white)}
.team-title em{font-style:normal;color:var(--green)}
.member{position:absolute;top:1439px;width:222px;text-align:center}
.portrait{width:222px;height:253px;border:4px solid var(--white);background:linear-gradient(#f3f3f3,#d9d9d9)}
.member.featured .portrait{background:var(--green);border-color:var(--green)}
.member h3{color:var(--white);font-size:16px;font-weight:700;margin-top:16px}
.member p{color:var(--green);font-size:12px;font-weight:700;line-height:19px;margin-top:4px}

/* how */
.how-photo{position:absolute;background:linear-gradient(135deg,#5f7283,#b9c4cc)}
.how-title{position:absolute;left:595px;top:1990px;font-size:32px;font-weight:700;color:var(--ink);line-height:40px}
.how-title em{display:block;font-style:normal;color:var(--green)}
.steps{position:absolute;left:595px;top:2078px;width:520px;list-style:none;font-size:13px;line-height:28px;color:#444;white-space:nowrap}
.steps li{position:relative;padding-left:24px}
.steps svg{position:absolute;left:0;top:8px}

/* portfolio */
.portfolio-bg{position:absolute;left:0;top:2655px;width:1200px;height:600px;background:var(--paper)}
.portfolio-title{position:absolute;left:0;top:2720px;width:1200px}
.logos{position:absolute;left:132px;top:2787px;display:flex;gap:8px}
.logo-tile{width:150px;height:67px;background:var(--white);display:flex;align-items:center;justify-content:center;font-size:18px;font-weight:700;color:#333}
.logo-tile.active{background:var(--green);color:var(--white)}
.story{position:absolute;left:172px;top:2900px;width:856px;height:227px;background:var(--white);border-radius:10px;box-shadow:0 8px 20px rgba(0,0,0,.12);text-align:center;padding:20px 20px 0}
.story p{font-size:13px;line-height:28px;white-space:nowrap}
.story .story-brand{font-size:32px;font-weight:800;color:var(--ink);margin-top:8px}

/* footer */
.footer-photo{position:absolute;left:0;top:3225px;width:1200px;height:441px;background:linear-gradient(120deg,#1a241d,#2a3a2e 55%,#182019)}
.footer-mark{position:absolute;left:176px;top:3365px;width:134px;height:134px;border-radius:50%;border:5px solid var(--white)}
.footer-name{position:absolute;left:132px;top:3510px;font-size:36px;font-weight:800;color:var(--white)}
.footer-col{position:absolute;top:3370px;color:var(--white)}
.footer-col h4{font-size:15px;font-weight:700;margin-bottom:10px}
.footer-col ul{list-style:none;font-size:13px;line-height:28px}
.subscribe{position:absolute;left:820px;top:3406px;width:246px;height:45px;background:var(--white);border-radius:3px;font-size:12px;color:#888;padding:13px 14px}
.social{position:absolute;left:824px;top:3495px;display:flex;gap:31px}
.social span{width:14px;height:14px;border-radius:50%;background:var(--white)}
.footer-rule{position:absolute;left:120px;top:3583px;width:932px;height:1px;background:rgba(255,255,255,.5)}
.legal{position:absolute;top:3598px;font-size:11px;font-weight:600;color:var(--white)}
.legal em{font-style:normal;color:var(--green)}
</style>
</head>
<body>

<header class="site-header">
  <div class="brand-box"><div class="brand-dot"></div><div class="brand-name">KESTREL.VC</div></div>
  <nav class="main-nav"><span>HOME</span><span>ABOUT US</span><span>WHAT</span><span>HOW</span><span>WHO</span><span>PORTFOLIO</span><span>CONTACT US</span></nav>
  <div class="call">
    <div class="call-icon"><svg width="18" height="18" viewBox="0 0 24 24"><path fill="#fff" d="M6.6 10.8a15 15 0 0 0 6.6 6.6l2.2-2.2c.3-.3.7-.4 1-.2 1.1.4 2.3.6 3.6.6.6 0 1 .4 1 1V20c0 .6-.4 1-1 1C10.6 21 3 13.4 3 4c0-.6.4-1 1-1h3.5c.6 0 1 .4 1 1 0 1.3.2 2.5.6 3.6.1.3 0 .7-.2 1z"/></svg></div>
    <div><div class="call-label">Call Us Today</div><div class="call-number">604 555 0147</div></div>
  </div>
</header>

<section class="hero">
  <div class="hero-photo" role="img" aria-label="Professional woman with arms crossed by an office window overlooking a city"></div>
  <svg class="abs" style="left:0;top:560px" width="1200" height="230" viewBox="0 0 1200 230">
    <path d="M0 160 C300 200 700 200 1120 90 L1200 60 L1200 230 L0 230Z" fill="#fff"/>
    <path d="M0 160 C300 215 720 200 1130 100 C800 230 300 225 0 200Z" fill="#7a9a2c"/>
  </svg>
  <div class="hero-circle">
    <h2>WELCOME TO</h2>
    <h1>KESTREL.VC</h1>
    <p>Kestrel.vc is a venture capital firm that invests in innovative<br>seed-stage technology companies in Western Canada focused<br>on B2B and SaaS markets.</p>
    <span class="btn">GET STARTED</span>
  </div>
  <div class="dots"><span></span><span></span><span></span><span></span></div>
</section>

<section class="about">
  <h2 class="section-title">ABOUT <em>KESTREL.VC</em></h2>
  <p class="about-lead">KESTREL.VC IS A VENTURE CAPITAL FIRM THAT INVESTS IN INNOVATIVE SEED-STAGE TECHNOLOGY<br>COMPANIES IN WESTERN CANADA FOCUSED ON B2B AND SAAS MARKETS.</p>
  <p class="about-body">Lorem ipsum dolor sit amet, consectetur adipiscing elit, sed do eiusmod tempor incididunt ut labore et dolore magna aliqua. Quis ipsum<br>suspendisse ultrices gravida. Risus commodo viverra maecenas accumsan lacus vel facilisis. Sed ut perspiciatis unde omnis iste natus<br>error sit voluptatem accusantium doloremque laudantium, totam rem aperiam, eaque ipsa quae ab illo inventore veritatis et quasi<br>architecto beatae vitae dicta sunt explicabo. Nemo enim ipsam voluptatem quia voluptas sit aspernatur aut odit aut fugit, sed quia<br>consequuntur magni dolores eos qui ratione voluptatem sequi nesciunt. Neque porro quisquam est, qui dolorem ipsum quia dolor sit amet,<br>consectetur, adipisci velit, sed quia non numquam eius modi tempora incidunt ut labore et dolore magnam .</p>
  <span class="btn">LEARN MORE ABOUT US</span>
</section>

<section class="team">
  <div class="team-photo" role="img" aria-label="Dark-toned team meeting scene behind the team section"></div>
  <svg class="abs" style="left:0;top:1230px" width="1200" height="720" viewBox="0 0 1200 720">
    <path d="M0 0 L1200 0 L1200 20 C900 10 500 20 80 140 L0 160Z" fill="#fff"/>
    <path d="M80 140 C500 20 900 10 1200 20 L1200 46 C900 40 500 40 80 140Z" fill="#7a9a2c"/>
    <path d="M0 720 L1200 720 L1200 600 C900 660 400 700 0 695Z" fill="#fff"/>
    <path d="M0 640 C400 670 850 640 1140 570 C900 660 400 700 0 700Z" fill="#7a9a2c"/>
  </svg>
  <h2 class="team-title">WHO WE ARE - <em>KESTREL TEAM</em></h2>
  <div class="member" style="left:132px"><div class="portrait" role="img" aria-label="Portrait of Owen Halloway"></div><h3>OWEN HALLOWAY</h3><p>GENERAL PARTNER,<br>FUNDS I AND II</p></div>
  <div class="member featured" style="left:370px"><div class="portrait" role="img" aria-label="Portrait of Ravi Deshan"></div><h3>RAVI DESHAN</h3><p>GENERAL PARTNER FUND<br>II, PARTNER FUND I</p></div>
  <div class="member" style="left:608px"><div class="portrait" role="img" aria-label="Portrait of Clara Vinter"></div><h3>CLARA VINTER</h3><p>GENERAL PARTNER,<br>FUNDS I AND II</p></div>
  <div class="member" style="left:845px"><div class="portrait" role="img" aria-label="Portrait of Jordan Pell"></div><h3>JORDAN PELL</h3><p>PARTNER FUND I</p></div>
</section>

<section class="how">
  <div class="how-photo" style="left:114px;top:2000px;width:448px;height:337px" role="img" aria-label="Founder thinking at a desk in an office"></div>
  <div class="how-photo" style="left:111px;top:2346px;width:451px;height:209px;background:linear-gradient(135deg,#d8d8d8,#8c8f93)" role="img" aria-label="Laptop, tablet and phone showing financial charts"></div>
  <h2 class="how-title">HOW WE MAKE<em>OUR VC INVESTMENTS</em></h2>
  <ul class="steps">
    <li><svg width="12" height="12" viewBox="0 0 12 12"><circle cx="6" cy="6" r="6" fill="#7a9a2c"/><path d="M4.5 3.5 7 6 4.5 8.5" stroke="#fff" stroke-width="1.5" fill="none"/></svg>We follow up on referrals to innovative technology companies at the<br>pre-seed or seed stage of funding</li>
    <li><svg width="12" height="12" viewBox="0 0 12 12"><circle cx="6" cy="6" r="6" fill="#7a9a2c"/><path d="M4.5 3.5 7 6 4.5 8.5" stroke="#fff" stroke-width="1.5" fill="none"/></svg>Before meeting, we'll review the company's investor pitch presentation and<br>its website</li>
    <li><svg width="12" height="12" viewBox="0 0 12 12"><circle cx="6" cy="6" r="6" fill="#7a9a2c"/><path d="M4.5 3.5 7 6 4.5 8.5" stroke="#fff" stroke-width="1.5" fill="none"/></svg>If we're interested, we'll meet with the founders in person or via call to get<br>their startup story</li>
    <li><svg width="12" height="12" viewBox="0 0 12 12"><circle cx="6" cy="6" r="6" fill="#7a9a2c"/><path d="M4.5 3.5 7 6 4.5 8.5" stroke="#fff" stroke-width="1.5" fill="none"/></svg>Together, we'll discuss the benefits of working with a venture firm and Kestrel<br>in particular</li>
    <li><svg width="12" height="12" viewBox="0 0 12 12"><circle cx="6" cy="6" r="6" fill="#7a9a2c"/><path d="M4.5 3.5 7 6 4.5 8.5" stroke="#fff" stroke-width="1.5" fill="none"/></svg>Afterward, we'll run the investment deal numbers and do preliminary due<br>diligence</li>
    <li><svg width="12" height="12" viewBox="0 0 12 12"><circle cx="6" cy="6" r="6" fill="#7a9a2c"/><path d="M4.5 3.5 7 6 4.5 8.5" stroke="#fff" stroke-width="1.5" fill="none"/></svg>If we want to move forward, we'll negotiate the deal structure and financing<br>terms with the founders</li>
    <li><svg width="12" height="12" viewBox="0 0 12 12"><circle cx="6" cy="6" r="6" fill="#7a9a2c"/><path d="M4.5 3.5 7 6 4.5 8.5" stroke="#fff" stroke-width="1.5" fill="none"/></svg>Then we'll give a term sheet to the company if it's selected as a prospective<br>Kestrel investment</li>
    <li><svg width="12" height="12" viewBox="0 0 12 12"><circle cx="6" cy="6" r="6" fill="#7a9a2c"/><path d="M4.5 3.5 7 6 4.5 8.5" stroke="#fff" stroke-width="1.5" fill="none"/></svg>We'll conduct in depth due diligence and draft our investment thesis sheet</li>
    <li><svg width="12" height="12" viewBox="0 0 12 12"><circle cx="6" cy="6" r="6" fill="#7a9a2c"/><path d="M4.5 3.5 7 6 4.5 8.5" stroke="#fff" stroke-width="1.5" fill="none"/></svg>Finally, we'll prepare and sign the legal agreements, the investment sheet,<br>and then fund the investment</li>
  </ul>
</section>

<section class="portfolio">
  <div class="portfolio-bg"></div>
  <h2 class="section-title portfolio-title">KESTREL FUND I <em>PORTFOLIO COMPANIES</em></h2>
  <div class="logos">
    <div class="logo-tile">loopline</div>
    <div class="logo-tile active">Fanrally.io</div>
    <div class="logo-tile" style="color:#aaa;font-weight:400;font-size:14px">Stillwave</div>
    <div class="logo-tile" style="font-size:14px">Tallypay</div>
    <div class="logo-tile">Nutriform</div>
    <div class="logo-tile" style="font-weight:400">Plainwork</div>
  </div>
  <div class="story">
    <p>Fanrally.io was acquired by Crowdkin in late 2020. Crowdkin is democratizing social data – to the benefit of everyone. They<br>began in 2018 as a platform for brands to find and reward their top fans. Now, they're leveling the playing field - giving<br>thousands of SMBs access to data only data scientists previously had access to. They are confident that the platform<br>they're providing is affordable, intuitive, and powerful.</p>
    <div class="story-brand">Fanrally.io</div>
  </div>
</section>

<footer>
  <div class="footer-photo" role="img" aria-label="Dark-toned office scene behind the footer"></div>
  <svg class="abs" style="left:0;top:3190px" width="1200" height="230" viewBox="0 0 1200 230">
    <path d="M0 0 L1200 0 L1200 35 C900 30 500 40 80 170 L0 200Z" fill="#f4f4f4"/>
    <path d="M80 170 C500 40 900 30 1200 35 L1200 62 C900 60 500 70 80 170Z" fill="#7a9a2c"/>
  </svg>
  <div class="footer-mark"></div>
  <div class="footer-name">KESTREL.VC</div>
  <div class="footer-col" style="left:417px"><h4>QUICK LINKS</h4><ul><li>Home</li><li>What</li><li>How</li><li>Who</li><li>Portfolio</li></ul></div>
  <div class="footer-col" style="left:611px"><h4>IMPORTANT</h4><ul><li>About Us</li><li>Contact Us</li><li>Sitmap</li><li>Privacy Policy</li></ul></div>
  <div class="footer-col" style="left:818px"><h4>SUBSCRIBE THE NEWSLETTERS</h4></div>
  <div class="subscribe">Enter The Email
    <svg class="abs" style="right:16px;top:14px" width="16" height="16" viewBox="0 0 16 16"><path d="M1 8 15 1 11 15 8 9Z" fill="#7a9a2c"/></svg>
  </div>
  <div class="social"><span></span><span></span><span></span><span></span><span></span></div>
  <div class="footer-rule"></div>
  <div class="legal" style="left:122px">© Copyrights 2021 <em>KESTREL.VC</em> &nbsp; | &nbsp; All Rights Reserved</div>
  <div class="legal" style="left:842px;font-weight:400">Privacy Policy &nbsp; | &nbsp; Term And Conditions</div>
</footer>

</body>
</html>
```